Organic skincare label - minimalist, earthy, luxe design needed!

I need a label design for a luxury natural skin care line called "Velka Botanix". Velka means 'earth' in Swahili. I would like the design to embody an earthy feel but be minimalistic and give a luxe vibe. My first product will be a Tumeric and Neem Scrub.

The size of the jar is 8oz, label dimensions should be (1.625" Tall x 8.5" Wide)
I will be making other products too such as; oils + toners so I feel free to do labels for glass bottles and/or spray bottles as well.

Forest green, light pinks/nudes/beige, grey, white, gold, are colors that can be used (not all have to be used).

I have included pictures of some things I've worked on myself as well as my original logo design but I need to simplify the logo, no circle around it.
Feel free to get creative.

Thank you! :)
Updates

Target Market(s)

Socially Conscious, Beauty Enthusiast, Minimalist

Industry/Entity Type

Skin Care

Font styles to use
Sans Serif
Other font styles liked:
• "Wonderlove doodle" is the font used for "Velka" in the logo. Feel free to use that or change it as you see fit.

Requirements
Must have
• Simplistic design
would like to stick to a font close to the ones in the logo. Either the one used for the name "Velka" OR the one that the slogan "earth's elixirs" uses.

I have also included some pictures to capture the aesthetic of my social media and website.

Gender neutral

```html
<!DOCTYPE html>
<html lang="en">
<head>
<meta charset="utf-8">
<title>Velka Botanix – Tumeric and Neem Scrub Labels</title>
<link rel="stylesheet" href="https://fonts.googleapis.com/css2?family=Old+Standard+TT:wght@400;700&family=Roboto:wght@400&family=Lato:wght@400&display=swap">
<style>
  :root {
    --page: #ffffff;
    --blush: #e2c3c3;
    --blush-soft: rgba(255, 255, 255, 0.28);
    --badge: #f1e4e3;
    --ink: #1f1b1b;
    --copper-dark: #955c34;
    --copper-light: #dca271;
    --band-text: #ffffff;
  }
  * { margin: 0; padding: 0; box-sizing: border-box; }
  html, body { width: 932px; height: 1200px; overflow: hidden; background: var(--page); }
  .sheet { position: relative; width: 932px; height: 1200px; }
  .panel { position: absolute; background: var(--blush); overflow: hidden; }
  .panel .shapes { position: absolute; inset: 0; width: 100%; height: 100%; }
  .lid { left: 0; top: 317px; width: 375px; height: 371px; }
  .front { left: 395px; top: 392px; width: 514px; height: 233px; }
  .wrap { left: 27px; top: 715px; width: 882px; height: 169px; }

  .badge { position: absolute; border-radius: 50%; background: var(--badge); }
  .brand-name {
    position: absolute; font-family: "Old Standard TT", serif; font-weight: 700;
    color: var(--ink); text-align: center; white-space: nowrap; transform: translateX(-50%);
  }
  .product-title {
    position: absolute; font-family: "Old Standard TT", serif; font-weight: 700;
    color: var(--ink); text-align: center; white-space: nowrap; transform: translateX(-50%);
    transform-origin: center; letter-spacing: -0.3px;
  }
  .line-band {
    position: absolute; color: var(--band-text); font-family: "Roboto", sans-serif;
    text-align: center; background: linear-gradient(90deg, var(--copper-dark), var(--copper-light) 55%, var(--copper-dark));
  }
  .net-vol { position: absolute; font-family: "Lato", sans-serif; color: var(--ink); text-align: center; transform: translateX(-50%); white-space: nowrap; }
  .copy {
    position: absolute; left: 375px; top: 19px; width: 285px;
    font-family: "Lato", sans-serif; font-size: 8.3px; line-height: 10.4px; color: var(--ink);
  }
  .code-area { position: absolute; left: 737px; top: 8px; width: 71px; height: 154px; background: #fff; }
</style>
</head>
<body>
<main class="sheet">

  <section class="panel lid" aria-label="Jar lid label">
    <svg class="shapes" viewBox="0 0 375 371" aria-hidden="true">
      <path fill="var(--blush-soft)" d="M230 120c40-30 100-30 110 10s-30 80-70 70-70-50-40-80z"/>
    </svg>
    <div class="badge" style="left:124px;top:124px;width:132px;height:132px;"></div>
    <div class="brand-name" style="left:190px;top:160px;font-size:44px;">Velka</div>
  </section>

  <section class="panel front" aria-label="Jar front label">
    <svg class="shapes" viewBox="0 0 514 233" aria-hidden="true">
      <path fill="var(--blush-soft)" d="M68 0h136c4 40-20 70-60 66S60 50 68 0z"/>
      <path fill="var(--blush-soft)" d="M330 40c40-10 70 20 60 60s-50 40-70 20-20-72 10-80z"/>
      <path fill="var(--blush-soft)" d="M320 233c-20-60 20-120 90-124s90 60 80 124z"/>
      <path fill="var(--blush-soft)" d="M100 120c40-20 80 0 80 50s-10 63-50 63-70-80-30-113z"/>
    </svg>
    <div class="badge" style="left:220px;top:22px;width:100px;height:100px;"></div>
    <div class="brand-name" style="left:270px;top:50px;font-size:30px;">Velka</div>
    <div class="product-title" style="left:270px;top:128px;font-size:27px;">Tumeric and Neem Scrub</div>
    <div class="line-band" style="left:139px;top:169px;width:262px;height:25px;font-size:21px;line-height:25px;">Velka Botanix</div>
    <div class="net-vol" style="left:270px;top:203px;font-size:11.5px;">net vol 240ml</div>
  </section>

  <section class="panel wrap" aria-label="Jar wraparound label">
    <svg class="shapes" viewBox="0 0 882 169" aria-hidden="true">
      <path fill="var(--blush-soft)" d="M48 0h98c4 30-10 44-40 40S40 20 48 0z"/>
      <path fill="var(--blush-soft)" d="M235 30c25-10 48 10 42 36s-40 26-50 10-12-38 8-46z"/>
      <path fill="var(--blush-soft)" d="M230 169c-14-50 20-90 60-90s44 50 40 90z"/>
      <path fill="var(--blush-soft)" d="M380 169c-8-40 30-60 60-56s50 30 56 56z"/>
      <path fill="var(--blush-soft)" d="M560 0h120c10 40-20 60-60 56s-70-30-60-56z"/>
    </svg>
    <div class="badge" style="left:160px;top:16px;width:72px;height:72px;"></div>
    <div class="brand-name" style="left:196px;top:34px;font-size:22px;">Velka</div>
    <div class="product-title" style="left:196px;top:92px;font-size:19px;">Tumeric and Neem Scrub</div>
    <div class="line-band" style="left:100px;top:123px;width:190px;height:17px;font-size:15px;line-height:17px;">Velka Botanix</div>
    <div class="net-vol" style="left:196px;top:149px;font-size:8.5px;">net vol 240ml</div>
    <p class="copy">Lorem ipsum dolor sit amet, consectetuer adipiscing elit, sed diam nonummy nibh euismod tincidunt ut laoreet dolore magna aliquam erat volutpat. Ut wisi enim ad minim veniam, quis nostrud exerci tation ullamcorper suscipit lobortis nisl ut aliquip ex ea commodo consequat. Duis autem vel eum iriure dolor in hendrerit in vulputate velit esse molestie consequat, vel illum dolore eu feugiat nulla facilisis at vero eros et accumsan et iusto odio dignissim qui blandit praesent luptatum zzril delenit augue duis dolore te feugait nulla facilisi.<br>Lorem ipsum dolor sit amet, cons ectetuer adipiscing elit, sed diam nonummy nibh euismod tincidunt ut laoreet dolore magna aliquam erat volutpat. Ut wisi enim ad minim veniam, quis nostrud exerci tation ullamcorper suscipit lobortis nisl ut aliquip ex ea commodo consequat.<br>Lomy nibh euismod tincidunt ut laoreet dolore magna aliquam erat vocipit</p>
    <div class="code-area" aria-hidden="true"></div>
  </section>

</main>
</body>
</html>
```